Lanternfield Billboard - Financial Services Company (Investments, Tax Planning and Insurance)

Our new office has a billboard directly above the office building. We'd like something eye-catching with a strong Call to Action, with the main part of the billboard being under 7 words if possible. We'd like you to include a way to get ahold of us (either our website lanternfieldllc.example or our phone number 302-418-2967. You may also include in small font something to indicate that we've been serving the area since 1980 (the DE area, the tri-state area, the Copperleaf Basin, etc.)

We offer financial planning, tax planning, and insurance, and we help our clients to focus on their goals and happiness by providing everything they need for lifelong wealth under one roof.

Our logos are attached, we use a triangle logo with green and gray. We use the tagline "experience lifelong wealth" but this does not need to be included.

Potential ideas we have seen from other financial companies-
- the concept that the driver spends more time looking at billboards than planning for their retirement
-something along the lines of "everything you need for your finances is in this building right here" planning, investments, taxes, insurance"
-don't spend your time worrying about retirement, let us help you plan for it
-are you working for your money, or is it working for you?
- retirement takes planning, we're here to help
- ready to retire? talk to us
- need investment advice?
- need help investing?
- crossing your fingers isn't a retirement plan. we can help.
- retiring soon? you need help.

Those are just general ideas, please feel free to be creative.

brand colors:
#00b585
#00b185
#000000
#ffffff
#6d6f75
#6d6f75
#6f7074
#021712
#052e24

```html
<!DOCTYPE html>
<html lang="en">
<head>
<meta charset="utf-8">
<title>Lanternfield Billboard</title>
<link href="https://fonts.googleapis.com/css2?family=Anton&family=Fjalla+One&display=swap" rel="stylesheet">
<style>
  :root {
    --brand-green: #02975f;
    --brand-deep: #042e25;
    --brand-gray: #6d6f75;
    --paper: #ffffff;
  }
  html, body {
    margin: 0;
    padding: 0;
    width: 1200px;
    height: 800px;
    overflow: hidden;
    background: var(--paper);
  }
  .canvas {
    position: relative;
    width: 1200px;
    height: 800px;
    background: var(--paper);
    overflow: hidden;
  }
  .billboard {
    position: absolute;
    left: 0;
    top: 200px;
    width: 1200px;
    height: 400px;
    background: var(--paper);
    box-shadow: 0 -6px 10px rgba(0,0,0,0.12), 0 6px 12px rgba(0,0,0,0.14);
  }
  .brand {
    position: absolute;
    left: 0;
    right: 0;
    top: 48px;
    text-align: center;
    font-family: "Anton", sans-serif;
    font-size: 40px;
    line-height: 1;
    letter-spacing: 1px;
    color: var(--brand-green);
  }
  .headline {
    position: absolute;
    left: 0;
    right: 0;
    margin: 0;
    text-align: center;
    font-family: "Anton", sans-serif;
    font-weight: 400;
    line-height: 1;
    white-space: nowrap;
    text-transform: uppercase;
    transform-origin: center top;
  }
  .headline--promise {
    top: 152px;
    font-size: 61px;
    color: var(--brand-green);
    transform: scaleX(1.52);
  }
  .headline--action {
    top: 246px;
    font-size: 75px;
    color: var(--brand-deep);
    transform: scaleX(1.5);
  }
  .contact-bar {
    position: absolute;
    left: 0;
    bottom: 0;
    width: 1200px;
    height: 34px;
    background: var(--brand-gray);
    color: var(--paper);
    font-family: "Fjalla One", sans-serif;
    display: flex;
    align-items: center;
    white-space: nowrap;
  }
  .service-area { position: absolute; left: 32px; font-size: 20px; }
  .contact-item {
    position: absolute;
    display: flex;
    align-items: center;
    gap: 8px;
    letter-spacing: 0.5px;
  }
  .contact-item--phone { left: 713px; font-size: 21px; }
  .contact-item--web { left: 922px; font-size: 17px; }
  .contact-icon { width: 18px; height: 18px; }
</style>
</head>
<body>
<div class="canvas">
  <section class="billboard">
    <div class="brand">Lanternfield</div>

    <h1 class="headline headline--promise">Financial Freedom Awaits</h1>
    <h2 class="headline headline--action">Start Planning Today</h2>

    <footer class="contact-bar">
      <span class="service-area">Proudly Serving the DE Area, Tri-State, Copperleaf Basin, etc. Since 1980</span>
      <span class="contact-item contact-item--phone">
        <svg class="contact-icon" viewBox="0 0 20 20" aria-hidden="true">
          <circle cx="10" cy="10" r="9.5" fill="#ffffff"/>
          <path d="M6.6 5.2l1.6-.4 1 2.4-1 .9c.5 1.2 1.4 2.1 2.6 2.6l.9-1 2.4 1-.4 1.6c-.2.5-.7.8-1.2.7-3.3-.5-5.9-3.1-6.4-6.4-.1-.6.2-1.2.5-1.4z" fill="#6d6f75"/>
        </svg>
        302-418-2967
      </span>
      <span class="contact-item contact-item--web">
        <svg class="contact-icon" viewBox="0 0 20 20" aria-hidden="true" fill="none" stroke="#ffffff" stroke-width="1.3">
          <circle cx="10" cy="10" r="8.5"/>
          <ellipse cx="10" cy="10" rx="3.8" ry="8.5"/>
          <line x1="1.5" y1="10" x2="18.5" y2="10"/>
          <line x1="10" y1="1.5" x2="10" y2="18.5"/>
          <path d="M3.2 5.5h13.6M3.2 14.5h13.6"/>
        </svg>
        WWW.LANTERNFIELDLLC.EXAMPLE
      </span>
    </footer>
  </section>
</div>
</body>
</html>
```